Etiketten-Design für Weinflasche
Greta hat mit sehr viel Mühe und Hingabe unsere Wünsche umgesetzt. Wir sind mit dem Endergebnis sehr zufrieden.
Zielgruppe
Wir sind ein Weingut-Startup und suchen ein frisches, hochwertiges Design für unsere Flaschenetiketten.
Aufgabenstellung
Wir benötigen ein Vorderetikett für unsere Weinflaschen mit folgenden Vorgaben:
- Etiketten sollen variabel nutzbar sein, für verschiedene Rebsorten bspw. in versch. Farben
- Auf dem Etikett zwingend: Logo (siehe Anlage), Rebsorte, Anbaugebiet (Nahe)
- Wiedererkennungswert
- nicht zu klassisch, nicht zu futuristisch (gutes Mittelmaß, wie beim Logo auch)
- ggf. Spiel mit (Hintergrund-)Farben für verschiedene Sorten, ggf. Hintergrundmuster (evtl. Höhenlinien des Tulmkopfs, Bad Kreuznach (unser Heimatberg))
- Anpassung an verschiedene Qualitätsstufen (Gutswein, Ortswein, Lagenwein), ggf. schwarzes Sonderetikett für absolutes Premiumsegment
- unsere Werte als Naturnah und familiengeführtes Weingut sollen transportiert werden
- Maß: 80x90mm (breitxhoch)
Insgesamt sind wir offen für verschiedene Vorschläge, auch wenn die Vorgaben oben teils sehr konkret sind. Bei guten Designs lassen wir uns gerne von unseren Vorstellungen abbringen ;)

```html
<!DOCTYPE html>
<html lang="de">
<head>
<meta charset="utf-8">
<title>Harlen Weingut – Etikett Reserva</title>
<link href="https://fonts.googleapis.com/css2?family=Playfair+Display:wght@400&family=Barlow+Condensed:wght@300;700&display=swap" rel="stylesheet">
<style>
  :root {
    --page: #ececee;
    --paper: #ffffff;
    --sand: #d6c4a1;
    --gold: #a88a4b;
    --wine: #7a3328;
    --blush: #d8c3bf;
    --white: #ffffff;
  }
  * { margin: 0; padding: 0; box-sizing: border-box; }
  html, body {
    width: 1200px; height: 1200px; overflow: hidden;
    background: var(--page);
  }
  .label {
    position: absolute;
    left: 130px; top: 72px;
    width: 940px; height: 1056px;
    background: var(--paper);
    overflow: hidden;
  }
  .landscape {
    position: absolute;
    left: 0; top: 600px;
    width: 100%; height: 456px;
    background: linear-gradient(to bottom, var(--blush) 0%, var(--wine) 32%, var(--wine) 100%);
  }
  .quality-band {
    position: absolute; left: 0; top: 0;
    width: 100%; height: 70px;
    background: var(--sand);
    display: flex; align-items: center; justify-content: center;
    font-family: "Barlow Condensed", sans-serif;
    font-weight: 300;
    font-size: 24px;
    letter-spacing: 0.22em;
    color: var(--white);
  }
  .variety {
    position: absolute;
    left: 128px; width: 688px;
    top: 238px;
    font-family: "Playfair Display", serif;
    font-weight: 400;
    font-size: 194px;
    line-height: 1;
    color: var(--gold);
    text-align: center;
    letter-spacing: -0.01em;
  }
  .variety__rule {
    position: absolute;
    left: 128px; width: 688px;
    top: 422px; height: 4px;
    background: var(--gold);
  }
  .region {
    position: absolute;
    left: 54px; top: 944px;
    font-family: "Barlow Condensed", sans-serif;
    font-weight: 700;
    font-size: 32px;
    letter-spacing: 0.3em;
    color: var(--white);
    line-height: 1;
  }
  .region__rule {
    position: absolute;
    left: 0; top: 990px;
    width: 174px; height: 2px;
    background: var(--white);
  }
  .brand {
    position: absolute;
    left: 410px; top: 890px;
    width: 470px;
    font-family: "Playfair Display", serif;
    font-weight: 400;
    font-size: 64px;
    line-height: 1;
    color: var(--white);
    text-align: center;
  }
</style>
</head>
<body>
  <main class="label">
    <div class="landscape" role="img" aria-label="Stilisierte Hügellandschaft des Heimatbergs in Weinrot und Altrosa"></div>

    <div class="quality-band">GUTSWEIN</div>

    <h1 class="variety">Reserva</h1>
    <div class="variety__rule"></div>

    <p class="region">NAHE</p>
    <div class="region__rule"></div>

    <p class="brand">Harlen Weingut</p>
  </main>
</body>
</html>
```